Bottle label design for a mulberry brandy

Please create a label design for a mulberry brandy. The registered brand name is "Kolvat"
The brandy will be produced in Armenia from 100% mulberry.
Color of the product: transparent.
The product will be sold worldwide. The price will be between 30 and 50 USD. So the product will be in premium category.
Therefore we need a solid design, appropriate to the product price category. The design, however, needs to be modern and optimistic.
You can have mulberries on the label or not have, it is up to you.
We have chosen for the product some bottle types, the links to the available bottles you can find in the attachment. Ideally you show a picture of your label on the bottle you selected.

Target Market(s)

worldwide

```html
<!DOCTYPE html>
<html lang="en">
<head>
<meta charset="utf-8">
<title>Kolvat Mulberry Brandy – Label</title>
<link rel="stylesheet" href="https://fonts.googleapis.com/css2?family=Playfair+Display:wght@900&family=Tinos:wght@400;700&family=Pinyon+Script&display=swap">
<style>
  :root {
    --stage: #ececec;
    --violet: #9900cc;
    --violet-deep: #7a00a6;
    --blush: #f7dcf8;
    --blush-deep: #eab8ee;
    --ink: #111111;
    --paper: #ffffff;
    --berry: #3a2f3f;
    --leaf: #8fc46a;
  }
  html, body {
    margin: 0;
    padding: 0;
    width: 1200px;
    height: 883px;
    overflow: hidden;
    background: var(--stage);
  }
  .canvas {
    position: relative;
    width: 1200px;
    height: 883px;
  }
  .label {
    position: absolute;
    left: 338px;
    top: 31px;
    width: 523px;
    height: 820px;
    display: block;
  }
  .brand-name {
    font-family: "Playfair Display", Georgia, serif;
    font-weight: 900;
    font-size: 70px;
    fill: var(--violet);
    letter-spacing: 1px;
  }
  .emblem-text {
    font-family: "Tinos", "Times New Roman", serif;
    font-size: 9.5px;
    letter-spacing: 1px;
    fill: var(--paper);
  }
  .tagline {
    font-family: "Tinos", "Times New Roman", serif;
    font-weight: 700;
    font-size: 16.5px;
    fill: var(--paper);
  }
  .quality {
    font-family: "Pinyon Script", cursive;
    font-size: 25px;
    fill: var(--ink);
  }
  .spec {
    font-family: "Tinos", "Times New Roman", serif;
    font-size: 12px;
    fill: var(--paper);
  }
</style>
</head>
<body>
<main class="canvas">
  <svg class="label" viewBox="0 0 421 660" xmlns="http://www.w3.org/2000/svg" aria-label="Kolvat mulberry brandy bottle label">
    <defs>
      <linearGradient id="fruit-tones" x1="0" y1="0" x2="0" y2="1">
        <stop offset="0" stop-color="#f4eef6"/>
        <stop offset="0.25" stop-color="#5a4a5e"/>
        <stop offset="0.7" stop-color="#3a2f3f"/>
        <stop offset="1" stop-color="#8fc46a"/>
      </linearGradient>
      <path id="emblem-arc" d="M175.4 140 A40 40 0 1 1 244.6 140"/>
    </defs>

    <!-- upper patterned field -->
    <path class="pattern-field" role="img" aria-label="Soft pink damask pattern background"
          d="M0 418 V140 L90 112 Q92 0 210 0 Q328 0 330 112 L421 140 V418 Z"
          fill="var(--blush)"/>

    <!-- lower colour band -->
    <rect class="color-band" x="0" y="418" width="421" height="242" fill="var(--violet)"/>

    <!-- outer frame -->
    <path class="frame-outer"
          d="M15 645 V150 L98 120 V100 Q98 13 210 13 Q322 13 322 100 V120 L405 150 V645 Z"
          fill="none" stroke="var(--ink)" stroke-width="1.6"/>

    <!-- inner thin frame lines with end dots -->
    <g class="frame-inner" stroke="var(--violet)" stroke-width="1.2" fill="var(--violet)">
      <path d="M27 375 V158 L94 134" fill="none"/>
      <path d="M394 375 V158 L327 134" fill="none"/>
      <circle cx="27" cy="375" r="2.2" stroke="none"/>
      <circle cx="394" cy="375" r="2.2" stroke="none"/>
      <circle cx="94" cy="134" r="2.2" stroke="none"/>
      <circle cx="327" cy="134" r="2.2" stroke="none"/>
    </g>

    <!-- emblem -->
    <g class="emblem">
      <circle cx="210" cy="120" r="88" fill="none" stroke="var(--ink)" stroke-width="1.4"/>
      <circle cx="210" cy="120" r="56" fill="var(--paper)" stroke="var(--ink)" stroke-width="1.6"/>
      <circle cx="210" cy="120" r="52" fill="var(--violet)"/>
      <circle class="emblem-art" role="img" aria-label="Line drawing of a mulberry branch"
              cx="210" cy="120" r="30" fill="var(--paper)" stroke="var(--violet-deep)" stroke-width="1"/>
      <text class="emblem-text" text-anchor="middle">
        <textPath href="#emblem-arc" startOffset="50%">MULBERRY BRANDY</textPath>
      </text>
    </g>

    <!-- brand name -->
    <text class="brand-name" x="210" y="288" text-anchor="middle">KOLVAT</text>

    <!-- fruit illustration area -->
    <rect class="fruit-art" role="img" aria-label="Illustration of ripe dark mulberries with white blossom and green leaves"
          x="178" y="308" width="96" height="168" rx="40" fill="url(#fruit-tones)"/>

    <!-- taglines -->
    <text class="tagline" x="210" y="520" text-anchor="middle">SMOOTH AND MELLOW TASTE</text>
    <text class="tagline" x="210" y="540" text-anchor="middle">PRODUCT OF ARMENIA</text>

    <!-- quality line -->
    <g class="quality-line">
      <line x1="120" y1="575" x2="134" y2="575" stroke="var(--ink)" stroke-width="1.6"/>
      <line x1="296" y1="575" x2="310" y2="575" stroke="var(--ink)" stroke-width="1.6"/>
      <text class="quality" x="215" y="582" text-anchor="middle">Premier Quality</text>
    </g>

    <!-- specs -->
    <g class="spec-alc">
      <path d="M48 565 Q57 559 66 565" fill="none" stroke="var(--paper)" stroke-width="1"/>
      <text class="spec" x="57" y="579" text-anchor="middle">40%</text>
      <text class="spec" x="57" y="594" text-anchor="middle">ALC</text>
      <path d="M48 602 Q57 608 66 602" fill="none" stroke="var(--paper)" stroke-width="1"/>
    </g>
    <g class="spec-volume">
      <path d="M363 565 Q372 559 381 565" fill="none" stroke="var(--paper)" stroke-width="1"/>
      <text class="spec" x="372" y="579" text-anchor="middle">750</text>
      <text class="spec" x="372" y="594" text-anchor="middle">ML</text>
      <path d="M363 602 Q372 608 381 602" fill="none" stroke="var(--paper)" stroke-width="1"/>
    </g>

    <!-- base rule -->
    <g class="base-rule" fill="var(--paper)">
      <line x1="28" y1="620" x2="387" y2="620" stroke="var(--paper)" stroke-width="1.4"/>
      <circle cx="28" cy="620" r="3.5"/>
      <circle cx="387" cy="620" r="3.5"/>
    </g>
  </svg>
</main>
</body>
</html>
```